Lunvaro Food Cafeteria and Food Services

I´m a Mexican Company , I dont know if we can built a US web page, but what we are a Cafeteria and Food Services, basically for industry , we produce food at companies for their employes, I have a Brochure to share if you consider. Our logo was made by your team. We need to have a Web page for our potentials custumers find us easy by internet

Target Market(s)

Food for manufacturers /Industry

Industry/Entity Type

Manufacturer

Number of Pages Required

4 page

Font styles to use
Sans Serif

Requirements
Must have
• Great images, Spanish and English options, our mision , vision , our actual customers , (be able to remove it also), our Certifications, our actual packages for services, our 90 days menu, our catering services, Contact page , Cafeteria Services , our meals serve now .
Nice to have
• Great pics, easy to access , and easy to move into the web page, nutricional ideas.
Should not have
• Fluorescent Color , or brilliant

```html
<!DOCTYPE html>
<html lang="en">
<head>
<meta charset="utf-8">
<title>Lunvaro — Cafeteria and Food Services</title>
<link href="https://fonts.googleapis.com/css2?family=Roboto:wght@300;400;500;700&family=Lora:ital,wght@0,400;1,400&display=swap" rel="stylesheet">
<style>
:root{
  --orange:#ff8a00;
  --orange-deep:#ff6d00;
  --orange-soft:#f39a1e;
  --green:#7cb342;
  --green-deep:#64a82c;
  --brown:#5a3516;
  --ink:#3d3d3d;
  --muted:#8a8a8a;
  --line:#e6e6e6;
  --paper:#ffffff;
  --mist:#f4f5f7;
}
*{box-sizing:border-box;margin:0;padding:0}
html,body{width:1200px;height:3285px;overflow:hidden}
body{position:relative;background:var(--paper);font-family:"Roboto",Arial,sans-serif;color:var(--ink)}
.abs{position:absolute}
.serif-italic{font-family:"Lora",Georgia,serif;font-style:italic}

/* header */
.site-header{position:absolute;left:0;top:0;width:1200px;height:145px;background:var(--paper)}
.call{position:absolute;left:85px;top:40px;display:flex;align-items:center;gap:14px;color:var(--green);font-size:19px;font-weight:500}
.call-icon{width:60px;height:60px;border:2px solid var(--green);border-radius:50%;display:flex;align-items:center;justify-content:center}
.brand{position:absolute;left:500px;top:44px;width:200px;display:flex;align-items:center;justify-content:center;gap:10px}
.brand-dot{width:22px;height:22px;border-radius:50%;background:var(--green)}
.brand-name{font-size:36px;font-weight:700;color:var(--brown);letter-spacing:.5px}
.lang{position:absolute;left:970px;top:48px;width:142px;height:44px;border:1px solid #d5d5d5;border-radius:4px;background:#fafafa;display:flex;align-items:center;padding:0 12px;gap:10px;font-size:13px;color:#444}
.lang-flag{width:20px;height:13px;background:#2b4a8b;border:1px solid #c9c9c9}
.lang svg{margin-left:auto}

/* nav */
.main-nav{position:absolute;left:0;top:145px;width:1200px;height:54px;background:var(--orange);display:flex;align-items:center;justify-content:space-between;padding:0 96px}
.main-nav a{color:#fff;text-decoration:none;font-size:11.5px;font-weight:500;letter-spacing:.3px;text-transform:uppercase}

/* hero */
.hero{position:absolute;left:0;top:199px;width:1200px;height:517px;overflow:hidden}
.hero-photo{position:absolute;inset:0;background:radial-gradient(ellipse at 50% 35%,#b88a52 0%,#7a5530 35%,#3f2a17 70%,#2a1c10 100%)}
.hero-photo::after{content:"";position:absolute;inset:0;background:linear-gradient(90deg,rgba(80,120,40,.35) 0%,rgba(0,0,0,0) 25%,rgba(0,0,0,0) 75%,rgba(80,120,40,.35) 100%)}
.hero-shade{position:absolute;inset:0;background:rgba(0,0,0,.28)}
.hero h1{position:absolute;left:0;width:1200px;top:126px;text-align:center;color:#fff;font-size:76px;font-weight:300;letter-spacing:1px}
.hero p{position:absolute;left:300px;width:600px;top:220px;text-align:center;color:#fff;font-size:15px;line-height:32px}
.btn-ghost{position:absolute;display:flex;align-items:center;justify-content:center;border:1px solid rgba(255,255,255,.85);color:#fff;font-size:12.5px;font-weight:500;text-transform:uppercase;letter-spacing:.3px;border-radius:3px}
.hero .btn-ghost{left:519px;top:342px;width:162px;height:44px;background:rgba(0,0,0,.15)}
.hero-arrow{position:absolute;top:235px;width:53px;height:53px;border-radius:50%;border:2px solid #fff;background:rgba(0,0,0,.25);display:flex;align-items:center;justify-content:center}

/* service cards */
.service-card{position:absolute;top:769px;width:330px;height:354px;border-radius:3px;color:#fff;text-align:center}
.service-card.orange{background:linear-gradient(180deg,#ff9d1e 0%,var(--orange-deep) 100%)}
.service-card.green{background:linear-gradient(180deg,#8fca45 0%,var(--green-deep) 100%)}
.service-icon{position:absolute;left:115px;top:18px;width:100px;height:118px;border-radius:12px;background:rgba(255,255,255,.22)}
.service-card h3{position:absolute;left:0;width:100%;top:154px;font-size:18px;font-weight:500;text-transform:uppercase}
.service-card p{position:absolute;left:28px;width:274px;top:190px;font-size:11px;line-height:24px}
.service-card .btn-ghost{left:105px;top:287px;width:120px;height:40px;font-size:11.5px}

/* mission */
.section-title{position:absolute;left:0;width:1200px;text-align:center;font-size:23px;font-weight:500;color:#4a4a4a;text-transform:uppercase;letter-spacing:.4px}
.section-sub{position:absolute;left:0;width:1200px;text-align:center;font-size:15.5px;color:var(--orange-soft)}
.section-copy{position:absolute;left:205px;width:790px;text-align:center;font-size:11.5px;line-height:27px;color:var(--muted)}
.btn-outline{position:absolute;display:flex;align-items:center;justify-content:center;border:1px solid var(--orange-soft);color:var(--orange-soft);font-size:12.5px;text-transform:uppercase;border-radius:3px}

/* coffee band */
.coffee-band{position:absolute;left:0;top:1441px;width:1200px;height:423px;overflow:hidden}
.coffee-photo{position:absolute;inset:0;background:linear-gradient(90deg,#e9e4dd 0%,#c8bdb0 22%,#6e4a2c 45%,#4a2d17 70%,#2e1b0d 100%)}
.coffee-photo::after{content:"";position:absolute;left:0;right:0;bottom:0;height:120px;background:linear-gradient(180deg,rgba(60,30,12,0) 0%,rgba(60,30,12,.85) 100%)}
.coffee-band h2{position:absolute;left:648px;top:82px;font-size:29px;font-weight:400;color:var(--orange);text-transform:uppercase}
.coffee-band p{position:absolute;left:648px;width:460px;top:128px;font-size:11.5px;line-height:26px;color:#fff}
.coffee-band .btn-ghost{left:652px;top:245px;width:170px;height:44px}

/* menu */
.menu-section{position:absolute;left:0;top:1864px;width:1200px;height:587px;background:var(--mist)}
.menu-card{position:absolute;width:500px;height:198px;background:#fff;border:1px solid var(--line);box-shadow:0 1px 3px rgba(0,0,0,.05)}
.menu-photo{position:absolute;left:15px;top:15px;width:171px;height:166px;border-radius:3px}
.menu-card h4{position:absolute;left:210px;top:28px;font-size:15.5px;font-weight:400;color:#333}
.menu-card p{position:absolute;left:210px;width:270px;top:60px;font-size:11px;line-height:24px;color:#666}
.menu-card .price{position:absolute;left:210px;top:142px;font-size:17px;color:var(--orange-soft);font-family:"Lora",Georgia,serif}

/* cafeteria band */
.cafe-band{position:absolute;left:0;top:2451px;width:1200px;height:392px;overflow:hidden}
.cafe-photo{position:absolute;inset:0;background:radial-gradient(ellipse at 30% 70%,#8a6a3a 0%,#4c5a2a 35%,#2f3a1e 65%,#1d2414 100%)}
.cafe-shade{position:absolute;inset:0;background:rgba(0,0,0,.45)}
.cafe-band h2{position:absolute;left:0;width:1200px;top:112px;text-align:center;font-size:24px;font-weight:500;color:#fff;text-transform:uppercase}
.cafe-band p{position:absolute;left:205px;width:790px;top:152px;text-align:center;font-size:11.5px;line-height:27px;color:#fff}
.cafe-band .btn-ghost{left:482px;top:262px;width:236px;height:45px}

/* partner strip */
.partner-strip{position:absolute;left:0;top:2843px;width:1200px;height:118px;background:var(--orange)}
.partner{position:absolute;top:22px;width:143px;height:74px;border:1px solid rgba(255,255,255,.55);display:flex;align-items:center;justify-content:center}
.partner span{width:96px;height:26px;border-radius:4px;background:rgba(255,255,255,.85)}

/* footer */
.site-footer{position:absolute;left:0;top:2961px;width:1200px;height:324px;background:#fff}
.footer-brand{position:absolute;left:110px;top:80px;display:flex;align-items:center;gap:10px}
.footer-brand .brand-dot{width:22px;height:22px}
.footer-brand .brand-name{font-size:38px}
.footer-col h5{position:absolute;font-size:14.5px;font-weight:500;color:#444;text-transform:uppercase;letter-spacing:.3px}
.contact-list{position:absolute;left:361px;top:76px;list-style:none}
.contact-list li{display:flex;align-items:center;gap:12px;height:27px;font-size:11px;color:#777}
.contact-list li.address{align-items:flex-start;height:auto;line-height:18px;padding-top:5px}
.contact-list a{color:#777}
.news-copy{position:absolute;left:631px;top:62px;width:215px;font-size:11px;line-height:22px;color:#777}
.news-input{position:absolute;left:631px;top:159px;width:212px;height:34px;border:1px solid #d8d8d8;font-size:11px;color:#888;padding:0 10px;display:flex;align-items:center}
.news-btn{position:absolute;left:631px;top:205px;width:82px;height:24px;background:#9ccc65;color:#fff;font-size:10px;text-transform:uppercase;display:flex;align-items:center;justify-content:center}
.follow-copy{position:absolute;left:900px;top:62px;width:205px;font-size:11px;line-height:20px;color:#777}
.social{position:absolute;top:155px;width:35px;height:35px;border:1px solid #cfcfcf;border-radius:50%}
.footer-rule{position:absolute;left:85px;top:248px;width:1030px;height:1px;background:var(--line)}
.copyright{position:absolute;left:0;width:1200px;top:276px;text-align:center;font-size:11px;color:#666}
</style>
</head>
<body>

<header class="site-header">
  <div class="call">
    <div class="call-icon">
      <svg width="26" height="26" viewBox="0 0 24 24" fill="none" stroke="#7cb342" stroke-width="2" stroke-linecap="round" stroke-linejoin="round"><path d="M22 16.9v3a2 2 0 0 1-2.2 2 19.8 19.8 0 0 1-8.6-3.1 19.5 19.5 0 0 1-6-6A19.8 19.8 0 0 1 2.1 4.2 2 2 0 0 1 4.1 2h3a2 2 0 0 1 2 1.7c.1.9.4 1.8.7 2.7a2 2 0 0 1-.5 2.1L8 9.8a16 16 0 0 0 6 6l1.3-1.3a2 2 0 0 1 2.1-.4c.9.3 1.8.6 2.7.7a2 2 0 0 1 1.7 2z"/></svg>
    </div>
    <span>Call us : (555) 014 2290</span>
  </div>
  <div class="brand"><span class="brand-dot"></span><span class="brand-name">Lunvaro</span></div>
  <div class="lang">
    <span class="lang-flag"></span><span>English</span>
    <svg width="10" height="6" viewBox="0 0 10 6"><path d="M1 1l4 4 4-4" stroke="#666" stroke-width="1.4" fill="none"/></svg>
  </div>
</header>

<nav class="main-nav">
  <a href="#">Home</a><a href="#">Mission</a><a href="#">Vision</a><a href="#">Customers</a><a href="#">Certifications</a><a href="#">Packages</a><a href="#">90 Day Menu</a><a href="#">Catering Services</a><a href="#">Cafeteria</a><a href="#">Meal Service</a><a href="#">Contact</a>
</nav>

<section class="hero">
  <div class="hero-photo" role="img" aria-label="Photo of a toasted sandwich with lettuce and tomatoes on a plate"></div>
  <div class="hero-shade"></div>
  <div class="hero-arrow" style="left:26px"><svg width="16" height="16" viewBox="0 0 16 16"><path d="M10 2L4 8l6 6" stroke="#fff" stroke-width="2" fill="none"/></svg></div>
  <div class="hero-arrow" style="left:1121px"><svg width="16" height="16" viewBox="0 0 16 16"><path d="M6 2l6 6-6 6" stroke="#fff" stroke-width="2" fill="none"/></svg></div>
  <h1>Lunvaro</h1>
  <p class="serif-italic">Sed ut perspiciatis unde omnis iste natus error sit voluptatem accusantium doloremque laudantium, totam rem aperiam, eaque ipsa quae ab illo inventore veritatis et quasi architecto beatae vitae dicta sunt explicabo.</p>
  <div class="btn-ghost">Read More Info</div>
</section>

<article class="service-card orange" style="left:85px">
  <div class="service-icon" role="img" aria-label="Icon of a waiter holding a serving dish"></div>
  <h3>Catering Services</h3>
  <p>Sed ut perspiciatis unde omnis iste natus error sit voluptatem accusantium doloremque laudantium, quae ab illo inventore vitae dicta sunt explicabo.</p>
  <div class="btn-ghost">View Details</div>
</article>
<article class="service-card green" style="left:436px">
  <div class="service-icon" role="img" aria-label="Icon of a server behind a cafeteria counter"></div>
  <h3>Cafeteria</h3>
  <p>Sed ut perspiciatis unde omnis iste natus error sit voluptatem accusantium doloremque laudantium, quae ab illo inventore vitae dicta sunt explicabo.</p>
  <div class="btn-ghost">View Details</div>
</article>
<article class="service-card orange" style="left:784px">
  <div class="service-icon" role="img" aria-label="Icon of a plate with fork and knife"></div>
  <h3>Meal Service</h3>
  <p>Sed ut perspiciatis unde omnis iste natus error sit voluptatem accusantium doloremque laudantium, quae ab illo inventore vitae dicta sunt explicabo.</p>
  <div class="btn-ghost">View Details</div>
</article>

<section class="mission">
  <h2 class="section-title" style="top:1182px">Our Mission &amp; Vision</h2>
  <p class="section-sub serif-italic" style="top:1222px">Sed ut perspiciatis unde omnis iste natus error sit voluptatem accusantium doloremque</p>
  <p class="section-copy" style="top:1252px">Nemo enim ipsam voluptatem quia voluptas sit aspernatur aut odit aut fugit, sed quia consequuntur magni dolores eos qui ratione voluptatem sequi nesciunt. Neque porro quisquam est, qui dolorem ipsum quia dolor sit amet, consectetur, adipisci velit, sed quia non numquam eius modi tempora enim ad minima veniam, quis nostrum exercitationem ullam corporis suscipit laboriosam.</p>
  <div class="btn-outline" style="left:519px;top:1358px;width:162px;height:48px">Read More Info</div>
</section>

<section class="coffee-band">
  <div class="coffee-photo" role="img" aria-label="Photo of a white coffee cup on a saucer with roasted coffee beans"></div>
  <h2>Services of Coffee Shops</h2>
  <p>Nemo enim ipsam voluptatem quia voluptas sit aspernatur aut odit aut fugit, sed quia consequuntur magni dolores eos qui ratione voluptatem sequi nesciunt. Neque porro quisquam est, qui dolorem ipsum quia dolor sit amet, consectetur</p>
  <div class="btn-ghost">Read More Info</div>
</section>

<section class="menu-section">
  <h2 class="section-title" style="top:32px">90 Day Menu</h2>
  <p class="section-sub serif-italic" style="top:69px">Sed ut perspiciatis unde omnis iste natus error sit voluptatem accusantium doloremque</p>

  <article class="menu-card" style="left:85px;top:124px">
    <div class="menu-photo" role="img" aria-label="Photo of grilled sandwiches" style="background:linear-gradient(135deg,#d9b06a,#7a5a2c)"></div>
    <h4>Sed ut perspiciatis unde omni</h4>
    <p>Sed ut perspiciatis unde omnis iste natus err or sit voluptatem accusantium dolorem quea ubea tae vitae dicta sunt explicabo.</p>
    <div class="price">$ 25.00</div>
  </article>
  <article class="menu-card" style="left:613px;top:124px">
    <div class="menu-photo" role="img" aria-label="Photo of fresh strawberries and blueberries with yogurt" style="background:linear-gradient(135deg,#f2e7e3,#c7303a 55%,#3b4a8a)"></div>
    <h4>Sed ut perspiciatis unde omni</h4>
    <p>Sed ut perspiciatis unde omnis iste natus err or sit voluptatem accusantium dolorem quea ubea tae vitae dicta sunt explicabo.</p>
    <div class="price">$ 25.00</div>
  </article>
  <article class="menu-card" style="left:85px;top:344px">
    <div class="menu-photo" role="img" aria-label="Photo of trays of hot food at a buffet" style="background:linear-gradient(135deg,#b58a48,#6d5a3a 50%,#3f4a2c)"></div>
    <h4>Sed ut perspiciatis unde omni</h4>
    <p>Sed ut perspiciatis unde omnis iste natus err or sit voluptatem accusantium dolorem quea ubea tae vitae dicta sunt explicabo.</p>
    <div class="price">$ 25.00</div>
  </article>
  <article class="menu-card" style="left:613px;top:344px">
    <div class="menu-photo" role="img" aria-label="Photo of a fresh green salad" style="background:linear-gradient(135deg,#e8d9a8,#8fb04a 50%,#4a3a22)"></div>
    <h4>Sed ut perspiciatis unde omni</h4>
    <p>Sed ut perspiciatis unde omnis iste natus err or sit voluptatem accusantium dolorem quea ubea tae vitae dicta sunt explicabo.</p>
    <div class="price">$ 25.00</div>
  </article>
</section>

<section class="cafe-band">
  <div class="cafe-photo" role="img" aria-label="Close-up photo of a salad with bread and greens"></div>
  <div class="cafe-shade"></div>
  <h2>Cafeteria &amp; Food Services</h2>
  <p>Nemo enim ipsam voluptatem quia voluptas sit aspernatur aut odit aut fugit, sed quia consequuntur magni dolores eos qui ratione voluptatem sequi nesciunt. Neque porro quisquam est, qui dolorem ipsum quia dolor sit amet, consectetur, adipisci velit, sed quia non numquam eius modi tempora enim ad minima veniam, quis nostrum exercitationem ullam corporis suscipit laboriosam</p>
  <div class="btn-ghost">Click Here For More Info</div>
</section>

<section class="partner-strip" aria-label="Current customers">
  <div class="partner" style="left:85px"><span></span></div>
  <div class="partner" style="left:263px"><span></span></div>
  <div class="partner" style="left:440px"><span></span></div>
  <div class="partner" style="left:618px"><span></span></div>
  <div class="partner" style="left:795px"><span></span></div>
  <div class="partner" style="left:972px"><span></span></div>
</section>

<footer class="site-footer">
  <div class="footer-brand"><span class="brand-dot"></span><span class="brand-name">Lunvaro</span></div>

  <div class="footer-col">
    <h5 style="left:361px;top:38px">Contact Us</h5>
    <ul class="contact-list">
      <li><svg width="13" height="13" viewBox="0 0 24 24" fill="#888"><path d="M6.6 10.8a15 15 0 0 0 6.6 6.6l2.2-2.2a1 1 0 0 1 1-.3 11.4 11.4 0 0 0 3.6.6 1 1 0 0 1 1 1V20a1 1 0 0 1-1 1A17 17 0 0 1 3 4a1 1 0 0 1 1-1h3.5a1 1 0 0 1 1 1 11.4 11.4 0 0 0 .6 3.6 1 1 0 0 1-.3 1z"/></svg>(555) 014 2290 (Phone)</li>
      <li><svg width="13" height="13" viewBox="0 0 24 24" fill="#888"><rect x="6" y="2" width="12" height="6"/><rect x="2" y="9" width="20" height="9" rx="2"/><rect x="6" y="15" width="12" height="7" fill="#fff" stroke="#888" stroke-width="2"/></svg>(555) 014 2290 (Fax)</li>
      <li><svg width="13" height="13" viewBox="0 0 24 24" fill="none" stroke="#888" stroke-width="2"><rect x="2" y="5" width="20" height="14"/><path d="M2 5l10 8 10-8"/></svg><a href="#">info@lunvaro.example</a></li>
      <li class="address"><svg width="13" height="13" viewBox="0 0 24 24" fill="#888"><path d="M12 2a7 7 0 0 0-7 7c0 5 7 13 7 13s7-8 7-13a7 7 0 0 0-7-7zm0 9.5A2.5 2.5 0 1 1 12 6.5a2.5 2.5 0 0 1 0 5z"/></svg><span>Av. Las Palmas 418 Col<br>Centro, Valle Norte B. C</span></li>
    </ul>
  </div>

  <div class="footer-col">
    <h5 style="left:631px;top:38px">Newsletter</h5>
    <p class="news-copy">Register Your email address to get information about us</p>
    <div class="news-input">Email Address</div>
    <div class="news-btn">Subscribe</div>
  </div>

  <div class="footer-col">
    <h5 style="left:900px;top:38px">Follow Us</h5>
    <p class="follow-copy">Lorem ipsum dolor sit amet; conse cetur adipiscing elit. Nulla in purus nibh. Donec ornare</p>
    <span class="social" style="left:900px"></span>
    <span class="social" style="left:943px"></span>
    <span class="social" style="left:986px"></span>
    <span class="social" style="left:1029px"></span>
    <span class="social" style="left:1072px"></span>
  </div>

  <div class="footer-rule"></div>
  <p class="copyright">© Copyright 2017 Lunvaro All Rights Reserved</p>
</footer>

</body>
</html>
```